Business Card Design Project

A dual branded business card.

We have 2 business's: keyLeap and keyLeap360º. keyLeap is an online education marketplace that helps students fid great courses and classes (from learn to surf, to vocational training courses).

keyLeap360º is an agency that helps primarily vocational course providers with their online marketing and student enrolments.

Target Market(s)

Manager and Marketing Manager / CEOs of VEPI, University, Vocational Course Providers (RTOs)

Industry/Entity Type

Education

Requirements
Must have
• Brett Holloway
CEO

7-19 Ferris Lane, Brackenvale Vic 3299
Phone: 1300 584 916
Mobile: 0417 298 605
Email: brett@keyleap.com.au

Both Logos
Nice to have
• I nice way to combine the 2 brands which act as related but separate business's.

Essentially keyLeap is a marketplace which enable schools to get more student leads through the keyLeap.com.au platform.

keyLeap360º is an agency where we deliver online marketing services including: Google / Facebook PPC, SEO, Retargeting, Website Development and design, Student Enrolment Intelligence, and more... Essentially and online agency specifically servicing the education sector.

keyLeap
Australia's Education Marketplace with over 2,500 Teachers and Schools Australia wide (subject to change)

keyLeap360º
Digital Marketing Education (subject to change)

Should not have
• Not cluttered, not cheap looking, needs to have digital agency quality...

```html
<!DOCTYPE html>
<html lang="en">
<head>
<meta charset="utf-8">
<title>keyLeap business card</title>
<link rel="stylesheet" href="https://fonts.googleapis.com/css2?family=Source+Sans+3:wght@400;700&display=swap">
<style>
  :root {
    --backdrop: #efe9e1;
    --card: #ffffff;
    --card-edge: #8a8a8a;
    --ink: #2b2b2b;
    --accent: #d58d22;
    --rule: #e0b35f;
    --brand: #7dbd32;
  }
  * { margin: 0; padding: 0; box-sizing: border-box; }
  html, body { width: 1200px; height: 1086px; overflow: hidden; }
  body {
    position: relative;
    background: var(--backdrop);
    font-family: "Source Sans 3", "Myriad Pro", Arial, sans-serif;
    color: var(--ink);
  }
  .card {
    position: absolute;
    background: var(--card);
    border: 1.5px solid var(--card-edge);
    border-radius: 32px;
    overflow: hidden;
  }
  .card--front { left: 65px; top: 65px; width: 796px; height: 455px; }
  .card--back  { left: 330px; top: 568px; width: 796px; height: 453px; }

  .brand-name {
    position: absolute;
    font-weight: 700;
    color: var(--brand);
    letter-spacing: -1px;
    line-height: 1;
    white-space: nowrap;
  }
  .card--front .brand-name { left: 49px; top: 52px; font-size: 78px; }
  .card--back .brand-name {
    left: 0; right: 0; top: 152px; text-align: center; font-size: 150px;
  }

  .divider {
    position: absolute; left: 0; top: 207px; width: 490px; height: 2px;
    background: var(--rule);
  }
  .name-tag {
    position: absolute; right: 0; top: 175px; width: 318px; height: 67px;
    background: var(--accent);
    border-radius: 34px 0 0 34px;
    color: #fff;
    font-size: 23px;
    line-height: 67px;
    padding-left: 30px;
    white-space: nowrap;
  }
  .name-tag strong { font-weight: 700; }
  .name-tag .role { font-size: 19px; }

  .contact { position: absolute; left: 54px; top: 252px; list-style: none; font-size: 22px; }
  .contact li { display: flex; align-items: center; height: 31px; }
  .contact svg { width: 16px; height: 16px; margin-right: 11px; fill: var(--ink); }
  .address { position: absolute; left: 54px; top: 372px; font-size: 22px; white-space: nowrap; }
</style>
</head>
<body>
  <section class="card card--front">
    <div class="brand-name">keyLeap360º</div>
    <div class="divider"></div>
    <div class="name-tag"><strong>Brett Holloway,</strong> <span class="role">CEO</span></div>
    <ul class="contact">
      <li>
        <svg viewBox="0 0 16 16" aria-hidden="true"><path d="M3 1l3 3-1.6 2a9 9 0 0 0 5.6 5.6L12 10l3 3-2 2C7 15 1 9 1 3z"/></svg>
        1300 584 916
      </li>
      <li>
        <svg viewBox="0 0 16 16" aria-hidden="true"><path d="M4 0h8v16H4zM5.5 2v8h5V2zM7 12v2h2v-2z"/></svg>
        0417 298 605
      </li>
      <li>
        <svg viewBox="0 0 16 16" aria-hidden="true"><path d="M0 6l8-5 8 5v9H0zM2 7l6 4 6-4-6-3.8z"/></svg>
        brett@keyleap.com.au
      </li>
    </ul>
    <p class="address">7-19 Ferris Lane, Brackenvale Vic 3299</p>
  </section>

  <section class="card card--back">
    <div class="brand-name">keyLeap</div>
  </section>
</body>
</html>
```